Complete collections of detective novels by Damien Valtrenoux

Cover for a NUMERIC book: all the 11 detective novels by Damien Valtrenoux.
Covers of these novels can be seen at https://www.editions-brunelle.example/auteur/damien-valtrenoux/ (but we don't want a patchwork).
All these books are connected with a medical atmosphere, they often include a beautiful women, some bandits and a detective.

Title: “The Cases of Dr. V – The Complete 2024”
Author: “Damien Valtrenoux”
Publisher: “Editions Brunelle”

Target Market(s)

Readers of detective novels

Requirements
Must have
• Adapted to screen (it's a digital book)

```html
<!DOCTYPE html>
<html lang="en">
<head>
<meta charset="utf-8">
<title>The Cases of Dr. V – The Complete 2024</title>
<link href="https://fonts.googleapis.com/css2?family=Cinzel:wght@400;700&family=Rubik+Dirt&family=Oswald:wght@300;500;700&display=swap" rel="stylesheet">
<style>
  :root {
    --canvas: #ffffff;
    --navy-deep: #0b1746;
    --navy: #15306e;
    --blue: #1d5697;
    --blue-soft: #4f7fb3;
    --mist: #c8d1dc;
    --floor: #e5e7eb;
    --floor-low: #d6d9de;
    --ink-light: #ffffff;
    --ink-dark: #141a33;
    --blood: #d8141f;
    --ice: #9fd3e0;
    --steel: #b9bcc0;
  }
  * { margin: 0; padding: 0; box-sizing: border-box; }
  html, body {
    width: 1200px; height: 1200px; overflow: hidden;
    background: var(--canvas);
  }
  .cover {
    position: absolute; left: 234px; top: 50px;
    width: 739px; height: 1107px; overflow: hidden;
    background: linear-gradient(180deg,
      var(--navy-deep) 0%, var(--navy) 22%, var(--blue) 42%,
      var(--blue-soft) 53%, var(--mist) 64%, var(--floor) 78%, var(--floor-low) 100%);
  }
  .publisher, .title, .subtitle, .author {
    position: absolute; left: 0; width: 100%; text-align: center;
  }
  .publisher {
    top: 58px; font-family: "Cinzel", serif; font-size: 29px;
    color: var(--ink-light); letter-spacing: 0.5px;
  }
  .title {
    top: 160px; font-family: "Rubik Dirt", sans-serif; font-size: 96px;
    line-height: 92px; color: var(--ink-light); letter-spacing: 2px; font-weight: 400;
  }
  .subtitle {
    top: 364px; font-family: "Cinzel", serif; font-size: 44px;
    color: var(--ink-light);
  }
  .author {
    top: 1056px; font-family: "Cinzel", serif; font-weight: 700;
    font-size: 24px; letter-spacing: 6px; color: var(--ink-dark);
  }
  .book {
    position: absolute; overflow: hidden;
    box-shadow: -4px 0 0 rgba(0,0,0,0.55), 6px 14px 18px rgba(0,0,0,0.35);
    font-family: "Oswald", sans-serif; color: var(--ink-light);
  }
  .book span { position: absolute; white-space: nowrap; display: block; }
  .book-author { font-weight: 500; }
  .book-title { font-weight: 700; text-transform: uppercase; }
  .red { color: var(--blood); }
  .book-imprint { font-size: 7px; font-weight: 300; color: #e8e8e8; }
</style>
</head>
<body>
  <main class="cover">
    <p class="publisher">Published by Editions Brunelle</p>
    <h1 class="title">THE CASES<br>OF DR. V</h1>
    <p class="subtitle">THE COMPLETE 2024</p>

    <div class="book" role="img" aria-label="Novel cover: figure in a long coat on a wet street" style="left:69px;top:470px;width:167px;height:120px;background:linear-gradient(160deg,#2a2a2a,#8a8a8a 60%,#d8d8d8);">
      <span class="book-title" style="left:22px;top:98px;font-size:13px;letter-spacing:1px;color:#222;">Homicide au bloc</span>
    </div>
    <div class="book" role="img" aria-label="Novel cover: close-up of an eye in red tones with palm trees" style="left:173px;top:489px;width:159px;height:217px;background:linear-gradient(150deg,#c4301c,#e07a3a 55%,#cfb79a);">
      <span class="book-author" style="left:58px;top:112px;font-size:15px;color:#2a1a14;">Valtrenoux</span>
      <span class="book-title" style="left:58px;top:134px;font-size:26px;color:#f3e6d8;">Crime</span>
    </div>
    <div class="book" role="img" aria-label="Novel cover: dark teal scene with a syringe" style="left:290px;top:507px;width:165px;height:200px;background:linear-gradient(160deg,#0d1517,#1f6a78 60%,#0e1a1e);">
      <span class="book-author" style="left:16px;top:18px;font-size:11px;line-height:13px;">Damien<br>Valtrenoux</span>
      <span class="book-title" style="left:16px;top:68px;font-size:18px;line-height:24px;"><b class="red">Poison</b> pour<br>bonnes <b class="red">raisons</b></span>
    </div>
    <div class="book" role="img" aria-label="Novel cover: man in sunglasses holding a gun" style="left:420px;top:526px;width:160px;height:183px;background:linear-gradient(160deg,#1d2735,#4c5866 55%,#27303b);">
      <span class="book-author" style="left:40px;top:10px;font-size:12px;color:var(--ice);">Damien Valtrenoux</span>
      <span class="book-title" style="left:24px;top:30px;font-size:26px;line-height:32px;font-weight:500;">Rançon<br>ou greffe</span>
    </div>
    <div class="book" role="img" aria-label="Novel cover: hospital corridor in pale blue" style="left:558px;top:558px;width:159px;height:262px;background:linear-gradient(160deg,#b8d8ec,#6ea4c8 55%,#dcecf5);">
      <span class="book-author" style="left:10px;top:45px;font-size:13px;color:#13305e;font-weight:700;">Damien Valtrenoux</span>
    </div>
    <div class="book" role="img" aria-label="Novel cover: woman in distress under a dark red title band" style="left:50px;top:589px;width:178px;height:286px;background:linear-gradient(170deg,#5a1010,#2a1a1a 45%,#3c3c3c);">
      <span class="book-title" style="left:34px;top:22px;font-family:'Cinzel',serif;font-size:20px;line-height:22px;text-align:center;">Dernier<br>crime<br>connu</span>
    </div>
    <div class="book" role="img" aria-label="Novel cover: old clinic among green hills" style="left:523px;top:651px;width:169px;height:280px;background:linear-gradient(170deg,#5f7a8a,#3f5a4a 50%,#2e4a52);">
      <span class="book-author" style="left:20px;top:10px;font-size:19px;line-height:23px;font-weight:300;color:var(--ice);">Damien<br>Valtrenoux</span>
      <span style="left:20px;top:66px;font-size:19px;font-weight:300;">L’Étrange Clinique</span>
    </div>
    <div class="book" role="img" aria-label="Novel cover: tagged foot in a morgue" style="left:97px;top:669px;width:178px;height:284px;background:linear-gradient(180deg,#0e0e10,#1a1a1e 45%,#7f95a6 75%,#d7e2ea);">
      <span class="book-author" style="left:40px;top:14px;font-size:14px;font-weight:700;">Damien Valtrenoux</span>
      <span class="book-title red" style="left:40px;top:40px;font-size:34px;line-height:38px;">Crime</span>
      <span class="book-title red" style="left:60px;top:80px;font-size:11px;">à la</span>
      <span class="book-title red" style="left:40px;top:94px;font-size:34px;line-height:38px;">Morgue</span>
      <span style="left:60px;top:142px;font-size:8px;font-style:italic;">suivi de La Rechute</span>
      <span class="book-imprint" style="left:80px;bottom:12px;color:#333;">Éditions Brunelle</span>
    </div>
    <div class="book" role="img" aria-label="Novel cover: silhouette with a shovel in a dark doorway" style="left:238px;top:706px;width:178px;height:285px;background:linear-gradient(180deg,#1a2a2c,#0f1a1c 55%,#3d6a78 75%,#0c1416);">
      <span class="book-title" style="left:22px;top:30px;font-size:36px;line-height:36px;color:var(--steel);">Une<br>nuit<br>de trop</span>
      <span class="book-title" style="left:20px;bottom:38px;font-size:14px;">Damien Valtrenoux</span>
      <span class="book-imprint" style="left:60px;bottom:14px;">Éditions Brunelle</span>
    </div>
    <div class="book" role="img" aria-label="Novel cover: leaf with blood drops on black" style="left:350px;top:725px;width:175px;height:284px;background:linear-gradient(180deg,#0e0e0e,#1b1b1b 50%,#2f5a22 72%,#111);">
      <span class="book-title" style="left:30px;top:8px;font-family:'Cinzel',serif;font-size:34px;">Dose</span>
      <span class="book-title" style="left:14px;top:52px;font-size:19px;line-height:22px;font-weight:300;text-align:center;">&nbsp;&nbsp;&nbsp;Sans<br>ordonnance</span>
      <span class="book-title" style="left:30px;bottom:36px;font-size:9px;letter-spacing:1.5px;font-weight:500;">Damien Valtrenoux</span>
      <span class="book-imprint" style="left:50px;bottom:14px;">Éditions Brunelle</span>
    </div>
    <div class="book" role="img" aria-label="Novel cover: woman in a black dress by railway tracks" style="left:496px;top:749px;width:177px;height:282px;background:linear-gradient(170deg,#150c0c,#3a2620 45%,#a89078 75%,#2a1c18);">
      <span class="book-author" style="left:20px;top:14px;font-size:14px;font-weight:700;">Damien Valtrenoux</span>
      <span class="book-title red" style="left:20px;top:36px;font-size:30px;">Crime</span>
      <span class="book-title red" style="left:20px;top:76px;font-size:20px;"><small style="font-size:9px;">par</small> précaution</span>
      <span class="book-imprint" style="left:70px;bottom:12px;">Éditions Brunelle</span>
    </div>

    <p class="author">DAMIEN VALTRENOUX</p>
  </main>
</body>
</html>
```